tri fold logistics company FLYER and A4 COMPANY FLYER COVER and A4 company flyer

we need to design company tri fold brochure and A4 company flyer cover for us
our company website is www.halvornfreight.com
pls design for us asap

ALSO OUR COMPANY NAME IS HALVORN FREIGHT INC
NOT " HALVORN FREIGHT, INC"

CAN YOU DESIGN THE COMPANY EMAIL SIGNATURE FOR US TOO

Target Market(s)

customer in U.S.

Industry/Entity Type

Freight Forwarding

Requirements
Must have
• company name and logo
• company name; HALVORN FREIGHT INC
Nice to have
• international shipping map,

```html
<!DOCTYPE html>
<html lang="en">
<head>
<meta charset="utf-8">
<title>Halvorn Freight Inc — Company Flyer</title>
<link href="https://fonts.googleapis.com/css2?family=Roboto:wght@400;500;700&family=Roboto+Condensed:wght@700&display=swap" rel="stylesheet">
<style>
  :root {
    --page-bg: #e9edf1;
    --header-bg: #f2f2f2;
    --ink: #2b2b2b;
    --yellow: #ffd200;
    --yellow-text: #f6c900;
    --panel-dark: #3d3d3d;
    --black: #0d0d0d;
    --white: #ffffff;
  }
  * { margin: 0; padding: 0; box-sizing: border-box; }
  html, body { width: 1200px; height: 1200px; overflow: hidden; background: var(--page-bg); }
  body { font-family: "Roboto", Arial, sans-serif; position: relative; }

  .flyer {
    position: absolute; left: 176px; top: 17px;
    width: 926px; height: 1274px;
    transform: scale(0.915); transform-origin: top left;
    background: var(--header-bg);
    overflow: hidden;
  }

  /* Header */
  .header { position: absolute; left: 0; top: 0; width: 926px; height: 180px; background: var(--header-bg); }
  .brand { position: absolute; left: 37px; top: 57px; display: flex; align-items: center; gap: 20px; }
  .brand-mark { width: 70px; height: 70px; border-radius: 50%; border: 3px solid #34304a; }
  .brand-name { font-size: 28px; font-weight: 500; color: #2a2740; letter-spacing: 0.5px; }
  .website { position: absolute; right: 40px; top: 75px; font-size: 24px; color: var(--ink); }
  .website .accent { color: var(--yellow-text); }
  .header-rule { position: absolute; left: 0; top: 180px; width: 926px; height: 6px; background: var(--yellow); }

  /* Hero */
  .hero { position: absolute; left: 0; top: 186px; width: 926px; height: 553px; }
  .hero-visual {
    position: absolute; inset: 0;
    background:
      radial-gradient(ellipse 55% 60% at 55% 55%, #a9a9a9 0%, #7a7a7a 45%, rgba(60,60,60,0) 80%),
      linear-gradient(135deg, #4a4a4a 0%, #6c6c6c 45%, #3a3a3a 100%);
  }
  .hero-title {
    position: absolute; right: 45px; top: 170px;
    font-family: "Roboto Condensed", "Arial Narrow", sans-serif; font-weight: 700;
    font-size: 46px; color: var(--yellow-text); line-height: 1;
  }
  .hero-band {
    position: absolute; left: 388px; width: 492px;
    background: rgba(255, 210, 0, 0.72); color: var(--white);
    font-family: "Roboto Condensed", "Arial Narrow", sans-serif; font-weight: 700;
    padding-left: 5px; white-space: nowrap; line-height: 1;
  }
  .hero-band.line-one { top: 226px; height: 48px; font-size: 37px; padding-top: 6px; }
  .hero-band.line-two { top: 281px; height: 63px; font-size: 59px; padding-top: 3px; }

  /* Lower section */
  .about-panel { position: absolute; left: 0; top: 739px; width: 444px; height: 514px; background: var(--panel-dark); color: var(--white); }
  .features-panel { position: absolute; left: 444px; top: 739px; width: 482px; height: 514px; background: var(--yellow); }
  .footer-bar { position: absolute; left: 0; top: 1253px; width: 926px; height: 21px; background: var(--black); }

  .section-title { font-size: 27px; font-weight: 700; line-height: 1; }
  .about-panel .section-title { position: absolute; left: 35px; top: 48px; }
  .title-rule { position: absolute; left: 32px; top: 84px; width: 102px; height: 2px; background: var(--yellow); }
  .about-copy { position: absolute; left: 35px; top: 103px; width: 337px; font-size: 12px; line-height: 14.4px; text-align: justify; color: #e8e8e8; }
  .about-copy p + p { margin-top: 4px; }
  .services-lead { position: absolute; left: 35px; top: 316px; font-size: 18px; color: var(--white); }
  .services-list { position: absolute; left: 56px; top: 367px; width: 280px; list-style: none; font-size: 12px; line-height: 14.5px; color: #e8e8e8; }
  .services-list li { position: relative; }
  .services-list li::before { content: "•"; position: absolute; left: -13px; color: var(--yellow); font-size: 10px; }

  .feature-icon {
    position: absolute; left: 385px; width: 112px; height: 112px; border-radius: 50%;
    background: var(--black); display: flex; align-items: center; justify-content: center;
  }
  .feature { position: absolute; left: 519px; width: 372px; }
  .feature .section-title { color: var(--white); }
  .feature p { margin-top: 9px; font-size: 12px; line-height: 14.4px; color: #2b2b2b; }
</style>
</head>
<body>
  <div class="flyer">
    <header class="header">
      <div class="brand">
        <span class="brand-mark"></span>
        <span class="brand-name">HALVORN FREIGHT INC</span>
      </div>
      <div class="website"><span class="accent">www.</span>halvornfreight<span class="accent">.com</span></div>
    </header>
    <div class="header-rule"></div>

    <section class="hero">
      <div class="hero-visual" role="img" aria-label="Grey-toned world map on a globe with glowing shipping routes connecting continents"></div>
      <div class="hero-title">HALVORN FREIGHT INC</div>
      <div class="hero-band line-one">YOUR SOLUTION TO ALL YOUR</div>
      <div class="hero-band line-two">SHIPPING NEEDS!</div>
    </section>

    <section class="about-panel">
      <h2 class="section-title">ABOUT US</h2>
      <div class="title-rule"></div>
      <div class="about-copy">
        <p>We leverage our service contracts and strong network of more than 150 agents around the world. Effective communication and flawless execution make our ocean service one of the most reliable and professional services in its class. We are confident that we can make shipping arrangements that are a perfect fit for your needs.</p>
        <p>We are an Ocean Transportation Intermediary (OTI) and Non-Vessel Operating Common Carrier (NVOCC) as licensed by the US Federal Maritime Commission. We are able to provide customs clearance at every US port under a national permit issued by the US Department of Homeland Security.</p>
      </div>
      <p class="services-lead">Our most common ocean services include:</p>
      <ul class="services-list">
        <li>FCL (Full Container Load) import and export</li>
        <li>LCL (Less-than-Container Load) import and export</li>
        <li>General cargo or Dangerous Goods</li>
        <li>Personal effects, residential pick up or delivery</li>
        <li>Marketora shpt importing from China or export Marketora shpt to UK</li>
      </ul>
    </section>

    <section class="features-panel"></section>

    <div class="feature-icon" style="top:786px">
      <svg width="50" height="32" viewBox="0 0 50 32" fill="none" stroke="#ffd200" stroke-width="2">
        <circle cx="25" cy="8" r="5"/><path d="M15 30v-7a10 8 0 0 1 20 0v7z"/>
        <circle cx="11" cy="11" r="4"/><path d="M2 30v-5a9 7 0 0 1 12-6"/>
        <circle cx="39" cy="11" r="4"/><path d="M48 30v-5a9 7 0 0 0-12-6"/>
      </svg>
    </div>
    <div class="feature-icon" style="top:941px">
      <svg width="52" height="52" viewBox="0 0 52 52" fill="none" stroke="#ffd200" stroke-width="2">
        <circle cx="26" cy="26" r="12" fill="#ffd200"/>
        <g stroke="#0d0d0d" stroke-width="1.5"><ellipse cx="26" cy="26" rx="5" ry="12"/><line x1="14" y1="26" x2="38" y2="26"/><line x1="16" y1="20" x2="36" y2="20"/><line x1="16" y1="32" x2="36" y2="32"/></g>
        <path d="M8 22a19 19 0 0 1 32-11"/><path d="M40 6v6h-6"/>
        <path d="M44 30a19 19 0 0 1-32 11"/><path d="M12 46v-6h6"/>
      </svg>
    </div>
    <div class="feature-icon" style="top:1096px">
      <svg width="44" height="40" viewBox="0 0 44 40" fill="#ffd200">
        <rect x="2" y="26" width="7" height="12"/><rect x="13" y="20" width="7" height="18"/>
        <rect x="24" y="24" width="7" height="14"/><rect x="35" y="14" width="7" height="24"/>
        <path d="M2 22 L14 12 L22 18 L34 6" fill="none" stroke="#ffd200" stroke-width="3"/>
        <path d="M30 2 L42 2 L42 14 Z"/>
      </svg>
    </div>

    <div class="feature" style="top:787px">
      <h3 class="section-title">LOREM IPSUM</h3>
      <p>dolor sit amet, consectetur adipiscing elit. Ut in magna vulputate, porta urna sed, facilisis nisi. Proin euismod efficitur odio vel luctus. Vivamus iaculis lacinia eros vitae ultricies.</p>
    </div>
    <div class="feature" style="top:941px">
      <h3 class="section-title">LOREM IPSUM</h3>
      <p>dolor sit amet, consectetur adipiscing elit. Ut in magna vulputate, porta urna sed, facilisis nisi. Proin euismod efficitur odio vel luctus. Vivamus iaculis lacinia eros vitae ultricies.</p>
    </div>
    <div class="feature" style="top:1105px">
      <h3 class="section-title">LOREM IPSUM</h3>
      <p>dolor sit amet, consectetur adipiscing elit. Ut in magna vulputate, porta urna sed, facilisis nisi. Proin euismod efficitur odio vel luctus. Vivamus iaculis lacinia eros vitae ultricies.</p>
    </div>

    <div class="footer-bar"></div>
  </div>
</body>
</html>
```